home accents e-commerce website

I'd like a professional simple website designed where I can sell my home goods. I already have my domain name registered. I need the website to accept credit card payments and Tendrix. It should have a shopping cart option and calculate sales tax and shipping costs on merchandise automatically.

I'll be taking photographs of the merchandise and writing product descriptions myself. (I'm not a professional photographer, so these photos probably won't look too polished. If you can help me make them look better, that'd be great). As I add new merchandise in the future, I'd like an option where I can log in to the back end myself and add pictures/product descriptions. And take old products down as they sell out. So the website needs to be user-friendly for me, even though I'm completely web design illiterate!

I'd like a creative, talented person who can create a whimsical, cute website. Nothing too corporate-looking.

Thank you!

Target Market(s)

women, online shoppers, New York City-area, (ship products to the United States only)

Industry/Entity Type

Home And Garden

Coding

Coded - Design and coding required

Number of Pages Required

1 page

Font styles to use
Sans Serif

Colors
0355a3
ffffff

Requirements
Must have
• shopping cart feature
• safe, secure credit card and Tendrix payments
• ability for me to go in and add new products and take down old/sold products
Nice to have
• whimsical, cute design
Should not have
• too corporate-looking

```html
<!DOCTYPE html>
<html lang="en">
<head>
<meta charset="utf-8">
<title>Alcove Home Goods</title>
<link rel="stylesheet" href="https://fonts.googleapis.com/css2?family=Lato:wght@400;700;900&family=Open+Sans:wght@400;600;700&display=swap">
<style>
:root{
  --blue:#0355a3;
  --white:#ffffff;
  --ink:#2b2b2b;
  --muted:#6f6f6f;
  --line:#dcdcdc;
  --panel:#f3f3f3;
  --price:#c8262b;
  --dark:#3b3436;
}
*{box-sizing:border-box;margin:0;padding:0}
html,body{width:1200px;height:2550px;overflow:hidden}
body{position:relative;background:var(--white);font-family:"Open Sans",Arial,sans-serif;color:var(--ink)}
a{color:inherit;text-decoration:none}
.abs{position:absolute}

/* top bar */
.topbar{position:absolute;top:0;left:0;width:1200px;height:41px;background:var(--blue);color:var(--white);font-size:12px}
.topbar .account-links{position:absolute;left:103px;top:12px;display:flex;gap:18px;white-space:nowrap}
.topbar .account-links span::before{content:"";display:inline-block;width:8px;height:8px;border-radius:50%;background:var(--white);margin-right:6px;vertical-align:0}
.topbar .social{position:absolute;right:150px;top:13px;display:flex;gap:14px;font-size:11px;white-space:nowrap}
.topbar .cart{position:absolute;left:1074px;top:8px}

/* header */
.header{position:absolute;top:41px;left:0;width:1200px;height:85px;background:var(--white)}
.brand{position:absolute;left:99px;top:14px;color:var(--blue);font-family:"Lato",sans-serif}
.brand .name{font-size:36px;font-weight:900;letter-spacing:1px;line-height:36px}
.brand .sub{font-size:12px;letter-spacing:3px;margin-top:2px}
.search{position:absolute;left:381px;top:27px;width:230px;height:31px;border:1px solid var(--line);border-radius:6px;font-size:10px;color:#9a9a9a;padding:8px 12px}
.search svg{position:absolute;right:10px;top:9px}
.nav{position:absolute;left:649px;top:35px;display:flex;gap:26px;font-size:13px;font-weight:400;color:var(--ink);text-transform:uppercase;white-space:nowrap}

/* hero */
.hero{position:absolute;top:126px;left:0;width:1200px;height:469px;background:linear-gradient(100deg,#5a2e22 0%,#8a4a34 30%,#6e3a2c 55%,#9b6a55 75%,#4e2a22 100%);color:var(--white);text-align:center;font-family:"Lato",sans-serif}
.hero h1{position:absolute;top:150px;width:100%;font-size:43px;font-weight:700;letter-spacing:.5px}
.hero p{position:absolute;top:223px;width:100%;font-size:21px}
.hero .btn{position:absolute;left:541px;top:299px;width:118px;height:43px;border:2px solid var(--white);border-radius:6px;font-size:14px;font-weight:700;line-height:39px}
.arrow-round{position:absolute;width:46px;height:46px;border-radius:50%;background:rgba(255,255,255,.35)}
.arrow-round svg{position:absolute;left:15px;top:14px}

/* shop */
.shop{position:absolute;top:595px;left:0;width:1200px;height:926px}
.side-head{background:var(--blue);color:var(--white);font-family:"Lato",sans-serif;font-weight:700;text-transform:uppercase;padding-left:20px}
.categories{position:absolute;left:99px;top:83px;width:234px;box-shadow:0 1px 4px rgba(0,0,0,.2)}
.categories .side-head{height:54px;line-height:54px;font-size:22px}
.categories li{list-style:none;height:50px;line-height:50px;border-bottom:1px solid var(--line);font-size:11px;font-weight:600;padding-left:20px;text-transform:uppercase;background:#fafafa}
.categories li::before{content:"» ";color:var(--ink)}
.newsletter{position:absolute;left:99px;top:624px;width:234px}
.newsletter .side-head{height:52px;line-height:52px;font-size:17px}
.newsletter p{font-size:11px;color:var(--muted);margin:22px 0 12px}
.newsletter .field{height:32px;border:1px solid #bdbdbd;font-size:11px;color:#8a8a8a;padding:8px;margin-bottom:13px}
.newsletter .subscribe{display:inline-block;margin-top:4px;width:108px;height:39px;border:2px solid var(--blue);border-radius:7px;color:var(--blue);font-size:11px;font-weight:700;text-align:center;line-height:35px}
.featured-tab{position:absolute;left:367px;top:83px;width:734px;height:52px;border-bottom:1px solid var(--line)}
.featured-tab span{display:inline-block;height:52px;padding:0 20px;background:var(--panel);color:var(--blue);font-size:16px;font-weight:600;line-height:52px;text-transform:uppercase}
.card{position:absolute;width:224px;height:262px;background:var(--white);box-shadow:0 1px 5px rgba(0,0,0,.22);text-align:center}
.card .photo{margin:3px;height:158px}
.card .price{margin-top:14px;color:var(--price);font-size:14px;font-weight:700}
.card .title{font-size:11px;font-weight:600;margin-top:4px}
.card .actions{display:flex;justify-content:center;gap:12px;margin-top:12px}
.card .actions i{display:block;width:26px;height:26px;border-radius:50%;border:1px solid var(--line);position:relative}
.card .actions svg{position:absolute;left:7px;top:7px}
.view-all{position:absolute;left:639px;top:794px;width:178px;height:47px;border:2px solid var(--blue);border-radius:8px;color:var(--blue);font-size:14px;font-weight:600;text-align:center;line-height:43px}

/* testimonial */
.testimonial{position:absolute;top:1521px;left:0;width:1200px;height:425px;background:linear-gradient(90deg,#4a3a3c 0%,#5e4a4e 35%,#6a4a58 60%,#3f3a3b 100%);color:var(--white);text-align:center}
.testimonial h2{position:absolute;top:58px;width:100%;font-family:"Lato",sans-serif;font-size:25px;font-weight:700}
.testimonial .quote{position:absolute;top:108px;left:290px;width:620px;font-size:11.5px;font-weight:600;line-height:23px}
.avatar{position:absolute;border-radius:50%}
.testimonial .person{position:absolute;top:336px;width:100%;font-size:14px;font-weight:700}
.testimonial .role{position:absolute;top:357px;width:100%;font-size:11px}

/* partners */
.partner{position:absolute;top:2030px;width:216px;height:107px;border:1px solid #cfcfcf;display:flex;align-items:center;justify-content:center;gap:10px;font-family:"Open Sans",sans-serif;font-size:24px;font-weight:700;color:#5a5a5a;white-space:nowrap}
.partner i{width:20px;height:20px;border-radius:50%;background:#8a8a8a}

/* footer */
.footer{position:absolute;top:2218px;left:0;width:1200px;height:332px;border-top:3px solid var(--blue)}
.fcol{position:absolute;top:63px}
.fcol h3{font-size:16px;font-weight:400;text-transform:uppercase;letter-spacing:.3px;margin-bottom:19px;color:var(--ink)}
.fcol li{list-style:none;font-size:11.5px;color:#4a4a4a;height:27px}
.fcol.links li::before{content:"» ";color:var(--blue)}
.fcol.follow li::before{content:"";display:inline-block;width:7px;height:7px;border-radius:50%;background:var(--blue);margin-right:12px}
.fcol.contact li{display:flex;gap:14px;height:auto;margin-bottom:20px;line-height:20px}
.fcol.contact svg{flex:none;margin-top:3px}
.footer .rule{position:absolute;top:244px;left:99px;width:1002px;border-top:1px dashed #bdbdbd}
.footer .copy{position:absolute;top:283px;left:99px;font-size:11px;color:#4a4a4a}
.pay{position:absolute;top:274px;right:99px;display:flex;gap:6px}
.pay span{height:32px;padding:0 9px;border:1px solid #c7c7c7;font-size:13px;font-weight:700;line-height:30px;color:var(--blue)}
</style>
</head>
<body>

<div class="topbar">
  <div class="account-links"><span>My Account</span><span>Wish List</span><span>Check Out</span></div>
  <div class="social"><span>Snapcove</span><span>Friendloop</span><span>Chirpline</span><span>Pinboardly</span></div>
  <svg class="cart" width="28" height="24" viewBox="0 0 28 24"><path d="M1 2h5l3 13h14l3-10H8" fill="none" stroke="#fff" stroke-width="2.4"/><rect x="9" y="5" width="16" height="9" fill="#fff"/><circle cx="11" cy="20" r="2.4" fill="#fff"/><circle cx="22" cy="20" r="2.4" fill="#fff"/></svg>
</div>

<header class="header">
  <div class="brand"><div class="name">alcove</div><div class="sub">HOME GOODS</div></div>
  <div class="search">Search here.......
    <svg width="11" height="11" viewBox="0 0 11 11"><circle cx="4.5" cy="4.5" r="3.5" fill="none" stroke="#999" stroke-width="1.4"/><path d="M7 7l3 3" stroke="#999" stroke-width="1.4"/></svg>
  </div>
  <nav class="nav"><a>About Alcove</a><a>How does this craziness work?</a><a>Contact</a></nav>
</header>

<section class="hero" role="img" aria-label="Warm bedroom scene with a wrought-iron bed, red bedding and wooden dressers">
  <h1>WELCOME TO ALCOVE HOME GOODS</h1>
  <p>Lorem Ipsum is simply dummy text of the printing</p>
  <a class="btn">BUY NOW</a>
  <div class="arrow-round" style="left:12px;top:204px"><svg width="14" height="18" viewBox="0 0 14 18"><path d="M11 2L4 9l7 7" fill="none" stroke="#fff" stroke-width="2.5"/></svg></div>
  <svg class="abs" style="left:1158px;top:216px" width="12" height="20" viewBox="0 0 12 20"><path d="M2 2l8 8-8 8" fill="none" stroke="#fff" stroke-width="2.5"/></svg>
</section>

<section class="shop">
  <aside class="categories">
    <div class="side-head">Categories</div>
    <ul>
      <li>Vases</li><li>Throw pillows</li><li>Blankets and throws</li><li>For your floors</li><li>For your walls</li><li>For your table</li><li>For your bedside</li><li>Let there be light</li><li>Put your feet up</li>
    </ul>
  </aside>

  <aside class="newsletter">
    <div class="side-head">Our Newsletter</div>
    <p>Your e-mail will be secure with us.</p>
    <div class="field">Name</div>
    <div class="field">Enter your mail</div>
    <a class="subscribe">SUBSCRIBE</a>
  </aside>

  <div class="featured-tab"><span>Featured Products</span></div>

  <div class="card" style="left:367px;top:177px"><div class="photo" role="img" aria-label="Yellow flowers in a white vase" style="background:linear-gradient(180deg,#e8e6ea,#d8c9a0 55%,#e9e6e3)"></div><div class="price">$199.00</div><div class="title">LOREM IPSUM IS SIMPLY</div><div class="actions"><i><svg width="12" height="12"><path d="M1 2h2l2 6h6l1-4H4" fill="none" stroke="#0355a3" stroke-width="1.6"/></svg></i><i><svg width="12" height="12"><path d="M6 11L1 6a3 3 0 015-4 3 3 0 015 4z" fill="#0355a3"/></svg></i><i><svg width="12" height="12"><path d="M2 10l8-8M6 2h4v4" fill="none" stroke="#0355a3" stroke-width="1.6"/></svg></i></div></div>
  <div class="card" style="left:622px;top:177px"><div class="photo" role="img" aria-label="White square pillow on grey" style="background:radial-gradient(circle,#f2f2f2 30%,#8d8d8d 75%)"></div><div class="price">$199.00</div><div class="title">LOREM IPSUM IS SIMPLY</div><div class="actions"><i><svg width="12" height="12"><path d="M1 2h2l2 6h6l1-4H4" fill="none" stroke="#0355a3" stroke-width="1.6"/></svg></i><i><svg width="12" height="12"><path d="M6 11L1 6a3 3 0 015-4 3 3 0 015 4z" fill="#0355a3"/></svg></i><i><svg width="12" height="12"><path d="M2 10l8-8M6 2h4v4" fill="none" stroke="#0355a3" stroke-width="1.6"/></svg></i></div></div>
  <div class="card" style="left:877px;top:177px"><div class="photo" role="img" aria-label="Bright bedroom with canopy bed and teal cushions" style="background:linear-gradient(180deg,#e9e4dc,#cfc6b8 60%,#b9a892)"></div><div class="price">$199.00</div><div class="title">LOREM IPSUM IS SIMPLY</div><div class="actions"><i><svg width="12" height="12"><path d="M1 2h2l2 6h6l1-4H4" fill="none" stroke="#0355a3" stroke-width="1.6"/></svg></i><i><svg width="12" height="12"><path d="M6 11L1 6a3 3 0 015-4 3 3 0 015 4z" fill="#0355a3"/></svg></i><i><svg width="12" height="12"><path d="M2 10l8-8M6 2h4v4" fill="none" stroke="#0355a3" stroke-width="1.6"/></svg></i></div></div>
  <div class="card" style="left:367px;top:483px"><div class="photo" role="img" aria-label="Orange velvet throw fabric" style="background:linear-gradient(135deg,#e07a12,#b5500a 50%,#e8861c)"></div><div class="price">$199.00</div><div class="title">LOREM IPSUM IS SIMPLY</div><div class="actions"><i><svg width="12" height="12"><path d="M1 2h2l2 6h6l1-4H4" fill="none" stroke="#0355a3" stroke-width="1.6"/></svg></i><i><svg width="12" height="12"><path d="M6 11L1 6a3 3 0 015-4 3 3 0 015 4z" fill="#0355a3"/></svg></i><i><svg width="12" height="12"><path d="M2 10l8-8M6 2h4v4" fill="none" stroke="#0355a3" stroke-width="1.6"/></svg></i></div></div>
  <div class="card" style="left:622px;top:483px"><div class="photo" role="img" aria-label="Red plaid blanket on a white sofa" style="background:linear-gradient(180deg,#e6e6e6,#c9c9c9 45%,#8a1f2a 70%,#d9d9d9)"></div><div class="price">$199.00</div><div class="title">LOREM IPSUM IS SIMPLY</div><div class="actions"><i><svg width="12" height="12"><path d="M1 2h2l2 6h6l1-4H4" fill="none" stroke="#0355a3" stroke-width="1.6"/></svg></i><i><svg width="12" height="12"><path d="M6 11L1 6a3 3 0 015-4 3 3 0 015 4z" fill="#0355a3"/></svg></i><i><svg width="12" height="12"><path d="M2 10l8-8M6 2h4v4" fill="none" stroke="#0355a3" stroke-width="1.6"/></svg></i></div></div>
  <div class="card" style="left:877px;top:483px"><div class="photo" role="img" aria-label="Stack of rolled colourful blankets" style="background:linear-gradient(180deg,#f0e8d8,#e36a8a 40%,#2bb3b0 65%,#e88a2a)"></div><div class="price">$199.00</div><div class="title">LOREM IPSUM IS SIMPLY</div><div class="actions"><i><svg width="12" height="12"><path d="M1 2h2l2 6h6l1-4H4" fill="none" stroke="#0355a3" stroke-width="1.6"/></svg></i><i><svg width="12" height="12"><path d="M6 11L1 6a3 3 0 015-4 3 3 0 015 4z" fill="#0355a3"/></svg></i><i><svg width="12" height="12"><path d="M2 10l8-8M6 2h4v4" fill="none" stroke="#0355a3" stroke-width="1.6"/></svg></i></div></div>

  <a class="view-all">VIEW ALL PRODUCTS</a>
</section>

<section class="testimonial" role="img" aria-label="Living room with floral curtains and a dark sofa">
  <h2>TESTIMONIAL</h2>
  <p class="quote">orem ipsum dolor sit amet, consectetur adipiscing elit, sed do eiusmod tempor incididunt ut labore et dolore magna aliqua. Ut enim ad minim veniam, quis nostrud exercitation ullamco laboris nisi ut</p>
  <div class="avatar" role="img" aria-label="Customer portrait" style="left:340px;top:204px;width:98px;height:98px;background:#b89a88"></div>
  <div class="avatar" role="img" aria-label="Customer portrait" style="left:422px;top:194px;width:116px;height:116px;background:#9a8f8c"></div>
  <div class="avatar" role="img" aria-label="Customer portrait" style="left:660px;top:194px;width:116px;height:116px;background:#a3928a"></div>
  <div class="avatar" role="img" aria-label="Customer portrait" style="left:762px;top:204px;width:98px;height:98px;background:#c4a590"></div>
  <div class="avatar" role="img" aria-label="Customer portrait" style="left:525px;top:181px;width:142px;height:142px;background:#c79a82;border:4px solid var(--white)"></div>
  <div class="person">MIRA LENZ</div>
  <div class="role">Manager</div>
  <div class="arrow-round" style="left:97px;top:233px;width:38px;height:38px"><svg width="12" height="14" viewBox="0 0 12 14" style="left:12px;top:12px"><path d="M9 1L3 7l6 6" fill="none" stroke="#fff" stroke-width="2.4"/></svg></div>
  <div class="arrow-round" style="left:1062px;top:233px;width:38px;height:38px"><svg width="12" height="14" viewBox="0 0 12 14" style="left:13px;top:12px"><path d="M3 1l6 6-6 6" fill="none" stroke="#fff" stroke-width="2.4"/></svg></div>
</section>

<div class="partner" style="left:99px"><i></i>Ledgerly</div>
<div class="partner" style="left:367px"><i></i>Filebay</div>
<div class="partner" style="left:624px"><i></i>Paywell</div>
<div class="partner" style="left:886px"><i></i>Shiftora</div>

<footer class="footer">
  <div class="fcol links" style="left:99px"><h3>Customer Service</h3><ul><li>About Us</li><li>Delivery Information</li><li>Privacy Policy</li><li>Terms &amp; Conditions</li></ul></div>
  <div class="fcol links" style="left:401px"><h3>My Account</h3><ul><li>My Account</li><li>Order History</li><li>Wish List</li><li>Newsletter</li></ul></div>
  <div class="fcol follow" style="left:690px"><h3>Follow Us</h3><ul><li>Friendloop</li><li>Chirpline</li><li>Workweb</li><li>Snapcove</li></ul></div>
  <div class="fcol contact" style="left:921px"><h3>Contact Us</h3><ul>
    <li><svg width="10" height="14" viewBox="0 0 10 14"><path d="M5 13S1 7.5 1 5a4 4 0 018 0c0 2.5-4 8-4 8z" fill="#0355a3"/><circle cx="5" cy="5" r="1.5" fill="#fff"/></svg><span>Old Simple Street, Old City,<br>New State</span></li>
    <li><svg width="12" height="12" viewBox="0 0 12 12"><path d="M2 1l3 2-1 2a7 7 0 003 3l2-1 2 3-2 2C5 11 1 7 0 3z" fill="#0355a3"/></svg><span>(+1) 555 010 2030</span></li>
    <li><svg width="12" height="10" viewBox="0 0 12 10"><rect width="12" height="10" fill="#0355a3"/><path d="M0 1l6 4 6-4" fill="none" stroke="#fff"/></svg><span>hello@alcovehome.test</span></li>
  </ul></div>
  <div class="rule"></div>
  <div class="copy">© Copyright 2017 Alcove. All Rights Reserved</div>
  <div class="pay"><span>Tendrix</span><span>Orbicard</span><span>Veyra</span><span>Amplex</span><span>Findpay</span></div>
</footer>

</body>
</html>
```